Business card

I need a business card design for my consulting company in animal welfare for livestock. I like clean, crisp, simple.

One I imagined was double-sided:
side1: just my name and contact information
side2: silhouette of farm animals. Could be 3 (pig, cow, chicken) or all the species (pig, cow, chicken, duck, sheep, rabbit, etc) that continue the length of the card. I have attached an image of a silhouette style.

But, I am open to any concept.

Industry/Entity Type

Business

```html
<!DOCTYPE html>
<html lang="en">
<head>
<meta charset="utf-8">
<title>Clara Whitmore – Business Card</title>
<link rel="stylesheet" href="https://fonts.googleapis.com/css2?family=Pacifico&family=Raleway:wght@300&family=Open+Sans:wght@400&display=swap">
<style>
  :root {
    --page-bg: #f1f1ef;
    --card-green: #63b946;
    --card-white: #ffffff;
    --silhouette-dark: #333a33;
    --silhouette-faint: #e6e6e6;
    --name-green: #5cb946;
    --text-grey: #4a4a4a;
    --text-dark: #2b2b2b;
  }
  * { box-sizing: border-box; margin: 0; padding: 0; }
  html, body {
    width: 1200px;
    height: 784px;
    overflow: hidden;
    background: var(--page-bg);
  }
  .canvas {
    position: relative;
    width: 1200px;
    height: 784px;
  }
  .card {
    position: absolute;
    top: 240px;
    width: 530px;
    height: 303px;
    box-shadow: 0 2px 6px rgba(0, 0, 0, 0.12);
    overflow: hidden;
  }
  .card--back {
    left: 50px;
    background: var(--card-green);
  }
  .card--front {
    left: 620px;
    background: var(--card-white);
  }
  .animal-row {
    position: absolute;
    left: 58px;
    top: 112px;
    width: 414px;
    height: 68px;
    border-radius: 30px;
    background: var(--silhouette-dark);
  }
  .animal-row--faint {
    left: 30px;
    top: 40px;
    width: 480px;
    height: 160px;
    border-radius: 0;
    background: radial-gradient(ellipse 50% 50% at 50% 50%,
      var(--silhouette-faint) 0%,
      rgba(230, 230, 230, 0.6) 45%,
      rgba(230, 230, 230, 0) 100%);
  }
  .identity {
    position: absolute;
    left: 112px;
    top: 70px;
  }
  .identity__name {
    font-family: "Pacifico", cursive;
    font-size: 42px;
    line-height: 1.15;
    color: var(--name-green);
    font-weight: 400;
  }
  .identity__tagline {
    margin-top: 0;
    font-family: "Raleway", sans-serif;
    font-weight: 300;
    font-size: 17px;
    color: var(--text-grey);
    letter-spacing: 0.2px;
    white-space: nowrap;
  }
  .contact {
    position: absolute;
    left: 282px;
    top: 196px;
    font-family: "Open Sans", sans-serif;
    color: var(--text-dark);
    font-style: normal;
    white-space: nowrap;
  }
  .contact__phone {
    font-size: 18px;
    letter-spacing: 0.5px;
  }
  .contact__email {
    margin-top: 8px;
    font-size: 14px;
    letter-spacing: 0.6px;
  }
</style>
</head>
<body>
  <main class="canvas">
    <section class="card card--back" aria-label="Card back">
      <div class="animal-row" role="img" aria-label="Row of dark farm animal silhouettes: sheep, rabbit, pig, duck, cow and rooster"></div>
    </section>

    <section class="card card--front" aria-label="Card front">
      <div class="animal-row animal-row--faint" role="img" aria-label="Faint grey farm animal silhouettes: sheep, cow and rooster"></div>
      <div class="identity">
        <h1 class="identity__name">Clara Whitmore</h1>
        <p class="identity__tagline">Welfare Services for Livestock Stakeholders</p>
      </div>
      <address class="contact">
        <p class="contact__phone">+1.555.214.0371</p>
        <p class="contact__email">clara.whitmore@fieldmail.com</p>
      </address>
    </section>
  </main>
</body>
</html>
```